3 screens for iOS app

I need a settings screen, dashboard and leaderboard screen created for an iPhone fitness app that is nearing completion. I have the template in .psd format that needs to be adhered to for consistency, and there are wireframe sketches (literally pen & paper) that you will translate into .psd files for chopping up and adding into the app. Also I need this by Monday.

Settings Screen:

Using the template psd, I need a basic list similar to the setting screen example attached (no icons needed, just text). The list of settings in order are:
Disclaimer
Edit Profile
Feedback
Help!
Terms of Use
Privacy Policy
Push Notifications (switcher icon on/off)
Chatterbook Posts (switcher icon on/off)
Quipster Posts (switcher icon on/off)
Lumora Viewtube Channel
Log Out

Dashboard:
The dashboard tempalte is attached. This dashboard should be inserted between the Grey banner heading and the Orange 14min standard routine bar. It will shift the graph down. The graph should remain unchanged, all you need to do in sert a cool looking dashboard inbetween the grey and orange bars

Dashboard contents:

Three dials (similar to stepmate, paceboard etc - see attached as an example) that display your progress

Dial 1: Title: Week
Dial should change colour as score approaches goal (ideally from green to orange as per icon example attached but not necessarily if you can make it look better)
Inside the dial it needs to include
Total: 598
Goal: 2,000
Days left: 5

Dial 2: Title: Improvement
Inside the dial it needs to include:
Start: 350
PB: 700
+100% in bold, centered

Dial 3: Title: Belt
Inside the dial needs to include:
Total: 9,834
Goal: 25,000

Leaderboard Screen:

Again using the template, with the grey banner heading at the top and tab bar at the bottom:

The leaderboard should be divided into two sections. The first is for my personal scores (as a user). The second section is for all players scores.

Section 1:
- Light grey background, dark grey text. Column titles can be pressed to filter columns. When pressed title changes colour from grey to orange (bold). If you can highlight two of the column titles orange that will be good

Section 2:
- White background, dark grey text. Column titles can be pressed to filter columns.
- Row height should be quite small to fit a large number of names on the screen.

Column titles: (sorry the wireframe sketch text is tough to read)
Rank / Name / W/outs / Wins / Week / Total / Belt

Rank - numeric values from 1-999
Name - text field
W/outs - number from 1-999
Wins - number 1-999
Week - number 1 - 99,999
Total - number 1- 99,999
Belt - coloured dot (white, black, red, blue, green, yellow)

For more info, refer http://www.lumora-example.co/ and download the old app (iphone only) for an idea what we're after.

Industry/Entity Type

Fitness

Colors
f68e4e

Requirements
Must have
• Use the .psd template provided. We're not looking for a redesign.
• The fonts are:
• LeckerliOne Regular
• LobsterTwo Bold
• MeriendaOne Regular
• MVBoli
• GothamExtraLight
• LobsterTwo
Nice to have
• The best dashboard of all time.
Should not have
• changes to fonts,

```html
<!DOCTYPE html>
<html lang="en">
<head>
<meta charset="utf-8">
<title>Lumora – Settings</title>
<link rel="stylesheet" href="https://fonts.googleapis.com/css2?family=Nunito+Sans:wght@400;600&family=Montserrat:wght@400;500&display=swap">
<style>
  :root {
    --bar-dark: #3d434b;
    --list-bg: #fafafa;
    --divider: #e3e3e3;
    --rail: #e8e8e8;
    --text-dark: #3a3f46;
    --text-light: #ffffff;
    --accent-orange: #f68e4e;
    --switch-on: #6ac52d;
    --switch-off: #3d434b;
    --battery: #4cd964;
    --tab-muted: #a4a9af;
    --tab-active: #ffffff;
    --results-green: #7ed321;
    --start-bg: #454b53;
    --start-ring: #5a6068;
  }
  * { box-sizing: border-box; margin: 0; padding: 0; }
  html, body { width: 1200px; height: 2206px; overflow: hidden; background: var(--list-bg); }
  body { position: relative; font-family: "Nunito Sans", sans-serif; color: var(--text-dark); }

  .status-bar {
    position: absolute; top: 0; left: 0; width: 1200px; height: 88px;
    background: var(--bar-dark); color: var(--text-light);
    font-family: "Montserrat", sans-serif; font-size: 40px; font-weight: 500;
  }
  .status-bar .signal { position: absolute; left: 20px; top: 26px; }
  .status-bar .clock { position: absolute; left: 0; width: 100%; top: 18px; text-align: center; }
  .status-bar .battery { position: absolute; right: 22px; top: 26px; }

  .nav-bar {
    position: absolute; top: 88px; left: 0; width: 1200px; height: 150px;
    background: var(--bar-dark); color: var(--text-light);
    font-family: "Montserrat", sans-serif;
  }
  .nav-bar .back { position: absolute; left: 30px; top: 48px; display: flex; align-items: center; gap: 18px; font-size: 58px; font-weight: 400; }
  .nav-bar .title { position: absolute; left: 0; width: 100%; top: 40px; text-align: center; font-size: 68px; font-weight: 400; }

  .settings-list {
    position: absolute; top: 238px; left: 0; width: 1200px; height: 1778px;
    display: flex; flex-direction: column; list-style: none; background: var(--list-bg);
  }
  .settings-list::before {
    content: ""; position: absolute; left: 28px; top: 0; bottom: 0; width: 2px; background: var(--rail);
  }
  .setting-row {
    position: relative; flex: 1; display: flex; align-items: center;
    padding-left: 116px; padding-right: 66px;
    font-size: 48px; border-bottom: 2px solid var(--divider);
  }
  .setting-row .label { flex: 1; }
  .setting-row.is-selected { background: var(--bar-dark); color: var(--text-light); border-bottom-color: var(--bar-dark); }
  .setting-row.is-selected::before {
    content: ""; position: absolute; left: 0; top: 0; bottom: 0; width: 26px; background: var(--accent-orange); z-index: 1;
  }
  .switch {
    width: 176px; height: 108px; border-radius: 54px; position: relative; background: var(--switch-off);
  }
  .switch::after {
    content: ""; position: absolute; top: 12px; left: 12px; width: 84px; height: 84px; border-radius: 50%; background: #fff;
  }
  .switch.is-on { background: var(--switch-on); }
  .switch.is-on::after { left: 80px; }

  .tab-bar {
    position: absolute; left: 0; bottom: 0; width: 1200px; height: 190px; background: var(--bar-dark);
  }
  .start-bump {
    position: absolute; left: 450px; top: -42px; width: 300px; height: 300px; border-radius: 50%;
    background: var(--start-bg); border: 3px solid var(--start-ring);
  }
  .tab-item {
    position: absolute; top: 0; width: 240px; height: 190px; margin-left: -120px;
    display: flex; flex-direction: column; align-items: center;
    font-family: "Montserrat", sans-serif; font-size: 36px; color: var(--tab-muted);
  }
  .tab-item svg { position: absolute; top: 24px; }
  .tab-item .tab-label { position: absolute; top: 126px; }
  .tab-item.is-active { color: var(--tab-active); }
  .tab-item.tab-start svg { top: 6px; }
</style>
</head>
<body>
  <header class="status-bar">
    <svg class="signal" width="180" height="40" viewBox="0 0 180 40" aria-hidden="true">
      <g fill="#fff">
        <circle cx="10" cy="18" r="9"/><circle cx="32" cy="18" r="9"/><circle cx="54" cy="18" r="9"/>
        <circle cx="76" cy="18" r="9"/><circle cx="98" cy="18" r="9"/>
      </g>
      <g fill="none" stroke="#fff" stroke-width="5" stroke-linecap="round">
        <path d="M120 12 a30 30 0 0 1 40 0"/><path d="M127 20 a20 20 0 0 1 26 0"/>
      </g>
      <circle cx="140" cy="30" r="5" fill="#fff"/>
    </svg>
    <div class="clock">9:00 AM</div>
    <svg class="battery" width="92" height="36" viewBox="0 0 92 36" aria-hidden="true">
      <rect x="2" y="2" width="80" height="32" rx="5" fill="none" stroke="#fff" stroke-width="3"/>
      <rect x="6" y="6" width="72" height="24" rx="3" fill="var(--battery)"/>
      <rect x="84" y="12" width="6" height="12" rx="2" fill="#fff"/>
    </svg>
  </header>

  <nav class="nav-bar">
    <div class="back">
      <svg width="34" height="58" viewBox="0 0 34 58" aria-hidden="true">
        <path d="M30 4 L6 29 L30 54" fill="none" stroke="#fff" stroke-width="6" stroke-linecap="round" stroke-linejoin="round"/>
      </svg>
      <span>Back</span>
    </div>
    <h1 class="title">Settings</h1>
  </nav>

  <ul class="settings-list">
    <li class="setting-row"><span class="label">Disclaimer</span></li>
    <li class="setting-row"><span class="label">Edit Profile</span></li>
    <li class="setting-row"><span class="label">Feedback</span></li>
    <li class="setting-row is-selected">
      <span class="label">Help!</span>
      <svg width="24" height="38" viewBox="0 0 24 38" aria-hidden="true">
        <path d="M4 4 L19 19 L4 34" fill="none" stroke="#fff" stroke-width="6" stroke-linecap="round" stroke-linejoin="round"/>
      </svg>
    </li>
    <li class="setting-row"><span class="label">Terms of Use</span></li>
    <li class="setting-row"><span class="label">Privacy Policy</span></li>
    <li class="setting-row"><span class="label">Push Notifications</span></li>
    <li class="setting-row"><span class="label">Chatterbook Posts</span><span class="switch is-on" role="switch" aria-checked="true"></span></li>
    <li class="setting-row"><span class="label">Quipster Posts</span><span class="switch" role="switch" aria-checked="false"></span></li>
    <li class="setting-row"><span class="label">Lumora Viewtube Channel</span><span class="switch" role="switch" aria-checked="false"></span></li>
    <li class="setting-row"><span class="label">Logout</span></li>
  </ul>

  <footer class="tab-bar">
    <div class="start-bump"></div>

    <div class="tab-item" style="left:110px">
      <svg width="96" height="96" viewBox="0 0 96 96" aria-hidden="true">
        <g fill="none" stroke="var(--tab-muted)" stroke-width="4">
          <ellipse cx="48" cy="30" rx="19" ry="24"/>
          <path d="M8 92 C10 68 24 60 36 56 M88 92 C86 68 72 60 60 56 M8 92 H88"/>
        </g>
      </svg>
      <span class="tab-label">Profile</span>
    </div>

    <div class="tab-item is-active" style="left:311px">
      <svg width="110" height="96" viewBox="0 0 110 96" aria-hidden="true">
        <g fill="none" stroke="var(--results-green)" stroke-width="6" stroke-linejoin="round" stroke-linecap="round">
          <path d="M6 78 L34 48 L50 64 L78 30 L92 44 L104 14"/>
          <path d="M6 90 L34 60 L50 76 L78 42 L92 56 L104 26" stroke-width="3"/>
        </g>
      </svg>
      <span class="tab-label">Results</span>
    </div>

    <div class="tab-item tab-start" style="left:600px">
      <svg width="110" height="120" viewBox="0 0 110 120" aria-hidden="true">
        <path d="M22 14 L96 60 L22 106 Z" fill="#8c9198" stroke="#8c9198" stroke-width="6" stroke-linejoin="round"/>
      </svg>
      <span class="tab-label">Start</span>
    </div>

    <div class="tab-item" style="left:878px">
      <svg width="96" height="100" viewBox="0 0 96 100" aria-hidden="true">
        <g fill="none" stroke="var(--tab-muted)" stroke-width="4" stroke-linejoin="round">
          <path d="M30 48 L14 92 L28 86 L36 98 L46 62"/>
          <path d="M66 48 L82 92 L68 86 L60 98 L50 62"/>
        </g>
        <circle cx="48" cy="30" r="26" fill="var(--accent-orange)"/>
        <text x="48" y="42" text-anchor="middle" font-family="Montserrat, sans-serif" font-size="34" font-weight="500" fill="#fff">2</text>
      </svg>
      <span class="tab-label">Challenges</span>
    </div>

    <div class="tab-item" style="left:1084px">
      <svg width="100" height="96" viewBox="0 0 100 96" aria-hidden="true">
        <path d="M20 90 L14 50 C12 30 22 12 40 8 L52 6 L56 20 L44 26 L42 46 C54 36 74 34 86 48 C94 60 90 80 78 88 Z"
              fill="none" stroke="var(--tab-muted)" stroke-width="4" stroke-linejoin="round"/>
      </svg>
      <span class="tab-label">Routines</span>
    </div>
  </footer>
</body>
</html>
```